Keystone Facility Partners Business card

We wish to have a professional Business card to present to large Corporate CEO's ASAP.

Our web site helps explain our business www.keystonefp.org

Keystone Facility Partners was established after we discovered how difficult it is to organise outsourced services while heading up a business or company.

We act as a facilitator for businesses who don't have the desire, expertise or recourses to manage their own systems and meet all their requirements.

We provide an all in one facility management solution for all types of businesses. We manage schedules, contractors and costs on behalf of businesses and their needs and wants.

Having an extensive network ensures we are able to connect businesses with the right service providers.

Target Market(s)

Company CEO

Industry/Entity Type

Business

Font styles to use
Sans Serif

Colors
33a6d7
f9fdfe
0355a3

Requirements
Must have
• professional design
Nice to have
• colours to match logo

```html
<!DOCTYPE html>
<html lang="en">
<head>
<meta charset="utf-8">
<title>Keystone Facility Partners – Business Card</title>
<link href="https://fonts.googleapis.com/css2?family=Lato:wght@300;400;700&display=swap" rel="stylesheet">
<style>
  :root {
    --sky: #33a6d7;
    --paper: #f9fdfe;
    --navy: #0355a3;
    --deep: #1f3f9a;
    --ink: #1d1d1f;
    --stage: #2e2e30;
  }
  * { margin: 0; padding: 0; box-sizing: border-box; }
  html, body { width: 1200px; height: 997px; overflow: hidden; }
  body {
    background: var(--stage);
    font-family: "Lato", sans-serif;
    position: relative;
  }
  .card {
    position: absolute;
    width: 580px;
    height: 330px;
    background: linear-gradient(135deg, #ffffff 0%, var(--paper) 55%, #e9eef1 100%);
    overflow: hidden;
  }
  .card--back { left: 70px; top: 130px; }
  .card--front { left: 550px; top: 500px; }

  .card__swoosh { position: absolute; inset: 0; width: 100%; height: 100%; }

  .brand {
    position: absolute;
    display: flex;
    align-items: center;
    gap: 12px;
  }
  .brand__dot {
    width: 26px; height: 26px;
    border-radius: 50%;
    background: var(--sky);
    flex: none;
  }
  .brand__name {
    font-weight: 700;
    color: var(--navy);
    letter-spacing: 0.06em;
    text-transform: uppercase;
    white-space: nowrap;
  }
  .card--back .brand { left: 70px; top: 142px; }
  .card--back .brand__name { font-size: 24px; }
  .card--front .brand { left: 150px; top: 48px; }
  .card--front .brand__name { font-size: 19px; }

  .name-bar {
    position: absolute;
    right: 0; top: 150px;
    width: 262px; height: 36px;
    border-radius: 18px 0 0 18px;
    background: linear-gradient(90deg, var(--navy), #1672c0);
    color: #bfe3f4;
    font-size: 18px;
    font-weight: 300;
    letter-spacing: 0.04em;
    display: flex; align-items: center;
    padding-left: 22px;
    text-transform: uppercase;
  }
  .name-bar__last { color: #ffffff; font-weight: 400; margin-left: 6px; }

  .contact-tab {
    position: absolute;
    left: 0; top: 200px;
    width: 50px; height: 112px;
    border-radius: 0 12px 12px 0;
    background: linear-gradient(180deg, #1672c0, var(--navy));
    display: flex; flex-direction: column;
    align-items: center; justify-content: space-around;
    padding: 10px 0;
  }
  .contact-tab svg { width: 22px; height: 22px; }

  .contact-list {
    position: absolute;
    left: 66px; top: 204px;
    list-style: none;
    color: var(--ink);
    font-size: 17px;
    line-height: 33px;
  }
</style>
</head>
<body>

  <section class="card card--back" aria-label="Card back">
    <svg class="card__swoosh" viewBox="0 0 580 330" aria-hidden="true">
      <path d="M330 330 C360 330 362 306 392 306 L580 292 L580 330 Z" fill="var(--deep)"/>
      <path d="M320 330 C352 330 354 312 388 310 L580 296 L580 300 L392 314 C364 316 360 330 340 330 Z" fill="#ffffff"/>
    </svg>
    <div class="brand">
      <span class="brand__dot"></span>
      <span class="brand__name">Keystone Facility Partners</span>
    </div>
  </section>

  <section class="card card--front" aria-label="Card front">
    <svg class="card__swoosh" viewBox="0 0 580 330" aria-hidden="true">
      <path d="M360 330 C388 330 390 306 420 304 L580 286 L580 330 Z" fill="var(--deep)"/>
      <path d="M350 330 C380 330 384 310 416 308 L580 290 L580 294 L420 312 C394 314 390 330 370 330 Z" fill="#ffffff"/>
    </svg>

    <div class="brand">
      <span class="brand__dot"></span>
      <span class="brand__name">Keystone Facility Partners</span>
    </div>

    <div class="name-bar">Daniel<span class="name-bar__last">Mercer</span></div>

    <div class="contact-tab">
      <svg viewBox="0 0 24 24" aria-label="Phone" role="img">
        <rect x="6" y="2" width="12" height="20" rx="2" fill="none" stroke="#fff" stroke-width="2"/>
        <line x1="10" y1="18" x2="14" y2="18" stroke="#fff" stroke-width="2"/>
      </svg>
      <svg viewBox="0 0 24 24" aria-label="Email" role="img">
        <rect x="2" y="5" width="20" height="14" rx="1" fill="#fff"/>
        <path d="M2 5 L12 13 L22 5" fill="none" stroke="#1672c0" stroke-width="1.6"/>
      </svg>
      <svg viewBox="0 0 24 24" aria-label="Website" role="img">
        <rect x="3" y="9" width="11" height="6" rx="3" transform="rotate(-45 8.5 12)" fill="none" stroke="#fff" stroke-width="2"/>
        <rect x="10" y="9" width="11" height="6" rx="3" transform="rotate(-45 15.5 12)" fill="none" stroke="#fff" stroke-width="2"/>
      </svg>
    </div>

    <ul class="contact-list">
      <li>0400 218 376</li>
      <li>www.keystonefp.org</li>
      <li>daniel@keystonefp.org</li>
    </ul>
  </section>

</body>
</html>
```